New women's health clinic needs a new home!!

We need a professional website for our modern women's health clinic. Needs to be in wordpress. Back end needs to be accesible by novice admin staff. Text and stock photography supplied by us. We need approximately 5 pages with 3-4 subpages each. Links to social media a must. Blog a must. Patients will need to be able to download e-books after supplying an e-mail address. Mobile-friendly is a must!

We created our logo through this site. Please refer to the logo for style themes.

Target Market(s)

Women aged 28-55

Industry/Entity Type

Health

Coding

Coded - Design and coding required

Number of Pages Required

5+ page

Font styles to use
Sans Serif

Colors
886aae
cee9f5
3377b5
d3a5cc
ffffff
eddcec
6e479c
85abd2
876aae

Requirements
Must have
• Wordpress
• Social media ready
• Mobile-friendly to Plivora's specs
• Ability to download e-books
• Captures data on back end

```html
<!DOCTYPE html>
<html lang="en">
<head>
<meta charset="utf-8">
<title>Aurelle Women's Health</title>
<link href="https://fonts.googleapis.com/css2?family=Open+Sans:wght@400;600;700&family=Raleway:wght@300;400;600;700&display=swap" rel="stylesheet">
<style>
:root{
  --purple:#6e479c;
  --violet:#886aae;
  --lilac:#d3a5cc;
  --blush:#eddcec;
  --sky:#cee9f5;
  --blue:#3377b5;
  --steel:#85abd2;
  --ink:#4a4a55;
  --muted:#77777f;
  --white:#ffffff;
  --foot:#f1f1f3;
  --foot-dark:#e2e2e6;
}
*{box-sizing:border-box;margin:0;padding:0}
html,body{width:1200px;height:3272px;overflow:hidden}
body{position:relative;background:var(--white);font-family:'Open Sans',Arial,sans-serif;color:var(--ink)}
.abs{position:absolute}
.center{text-align:center}
.photo{background:linear-gradient(120deg,var(--blush),var(--lilac) 45%,var(--sky))}
.circle{border-radius:50%;overflow:hidden;border:6px solid var(--white);box-shadow:0 3px 10px rgba(110,71,156,.25)}
.btn{display:inline-block;background:var(--violet);color:var(--white);font-size:11px;font-weight:600;letter-spacing:.5px;padding:7px 20px;border-radius:2px;text-transform:uppercase}
.heading{font-family:'Raleway',Arial,sans-serif;font-size:30px;letter-spacing:1px;text-transform:uppercase;color:var(--purple);font-weight:700}
.heading span{font-weight:300;color:var(--violet)}
.kicker{font-family:'Raleway',Arial,sans-serif;font-size:15px;letter-spacing:2px;color:var(--violet);text-transform:uppercase}
.copy{font-size:13px;line-height:1.7;color:var(--muted)}

/* top */
.topbar{left:0;top:0;width:1200px;height:32px;background:var(--white);border-bottom:1px solid var(--blush)}
.topbar .dots{left:40px;top:10px;display:flex;gap:8px}
.topbar .dots i{width:12px;height:12px;border-radius:50%;background:var(--violet);display:block}
.topbar .phone{right:40px;top:8px;font-size:11px;color:var(--purple)}
.hero{left:0;top:32px;width:1200px;height:470px;background:linear-gradient(100deg,#f4eef7 0%,#e6cfe6 30%,#d9c2e0 55%,#cfe6d9 80%,#e9f3ee 100%)}
.nav{left:0;top:32px;width:1200px;height:40px;background:rgba(255,255,255,.85);font-size:12px}
.nav ul{list-style:none;position:absolute;top:12px;display:flex;gap:28px;color:var(--ink)}
.nav .left{left:40px}.nav .right{right:40px}
.nav .active{background:var(--violet);color:var(--white);padding:4px 10px;margin-top:-4px}
.logo-mark{left:548px;top:6px;width:104px;height:104px;background:radial-gradient(circle at 40% 35%,var(--white),var(--lilac) 60%,var(--violet));}
.brand{left:0;top:118px;width:1200px;font-family:'Raleway',Arial,sans-serif;font-weight:700;font-size:32px;line-height:1.05;color:#3a2f4a;letter-spacing:1px}
.hero-text{left:400px;top:262px;width:400px}
.hero-text .small{font-family:'Raleway',Arial,sans-serif;font-size:14px;color:var(--white);letter-spacing:2px}
.hero-text .big{font-family:'Raleway',Arial,sans-serif;font-size:26px;font-weight:700;color:var(--purple);letter-spacing:1px}
.hero-text p{font-size:12px;line-height:1.6;color:var(--white);margin:10px 0 18px}
.curve{left:0;top:440px;width:1200px;height:70px}

/* welcome */
.service-icon{width:124px;height:124px}
.tag{font-size:11px;font-weight:700;color:var(--purple);text-transform:uppercase;line-height:1.3}

/* bands */
.band{left:0;width:1200px}
.edge{left:0;width:1200px}
.service-card{width:170px}
.service-card .circle{width:160px;height:160px;margin:0 auto}
.service-card .copy{font-size:11px;margin-top:16px;line-height:1.6}
.badge{width:60px;height:60px;border-radius:50%;background:var(--violet);border:3px solid var(--white);color:var(--white);font-size:8px;font-weight:700;display:flex;align-items:center;justify-content:center;text-align:center;line-height:1.2;text-transform:uppercase}
.post{width:180px}
.post h4{font-size:12px;font-weight:700;color:var(--ink);margin:12px 0 8px;line-height:1.4;text-transform:uppercase}
.arrow{width:20px;height:30px}
.social{width:220px}
.social .dot{width:58px;height:58px;border-radius:50%;margin:0 auto 12px}
.social .name{font-size:12px;font-weight:700;color:var(--purple)}
.social p{font-size:11px;color:var(--muted);line-height:1.6;margin-top:6px}

/* footer */
.footer{left:0;top:3040px;width:1200px;height:180px;background:var(--foot)}
.fcol h5{font-size:11px;font-weight:700;text-transform:uppercase;color:var(--ink);margin-bottom:10px}
.fcol li{list-style:none;font-size:11px;color:var(--muted);line-height:1.9}
.subscribe{left:760px;top:3050px;width:290px;height:160px;background:var(--white);border:1px solid var(--foot-dark);padding:14px}
.subscribe input{display:block;width:100%;height:24px;border:1px solid var(--foot-dark);margin:8px 0;font-size:10px;padding:0 6px;font-family:inherit}
.bottombar{left:0;top:3220px;width:1200px;height:52px;background:var(--foot-dark);font-size:11px;color:var(--muted);padding:19px 150px}
</style>
</head>
<body>

<!-- header & hero -->
<div class="abs hero" role="img" aria-label="Soft focus photo of a smiling woman in pastel pink and green light"></div>
<div class="abs topbar">
  <div class="abs dots"><i></i><i></i><i></i></div>
  <div class="abs phone">(02) 4000 1234</div>
</div>
<nav class="abs nav">
  <ul class="left"><li class="active">Home</li><li>Healthcare Services</li><li>Team</li><li>Fees</li></ul>
  <ul class="right"><li>Testimonials</li><li>Videos</li><li>Blog</li><li>E-book</li><li>Contact</li></ul>
</nav>
<div class="abs circle logo-mark" role="img" aria-label="Clinic emblem"></div>
<div class="abs brand center">AURELLE<br>WOMEN'S HEALTH</div>
<div class="abs hero-text center">
  <div class="small">WOMEN'S HEALTH</div>
  <div class="big">PERFECT HEALTH</div>
  <p>Caring support for every stage of life, from routine checks to planning a family, with a team who listens and takes time with you.</p>
  <span class="btn">Read More</span>
</div>
<svg class="abs curve" viewBox="0 0 1200 70" preserveAspectRatio="none"><path d="M0 70 L0 62 Q600 -10 1200 62 L1200 70Z" fill="#fff"/></svg>
<div class="abs circle" style="left:550px;top:430px;width:100px;height:100px;background:linear-gradient(135deg,#f2f2f4,#b9b7c4)" role="img" aria-label="Stethoscope photo"></div>

<!-- welcome -->
<div class="abs center" style="left:0;top:596px;width:1200px">
  <div class="kicker">Welcome to</div>
  <div class="heading" style="margin-top:4px">Aurelle Women's Health</div>
</div>
<p class="abs copy center" style="left:300px;top:672px;width:600px">Our clinic offers thoughtful, modern care for women at every age. We bring together experienced doctors and nurses to look after your wellbeing, answer your questions and help you feel confident about your health choices today.</p>
<div class="abs center" style="left:378px;top:770px">
  <div class="circle service-icon photo" role="img" aria-label="Photo of two smiling women"></div>
  <div class="tag" style="margin-top:12px">Well Woman<br>Check</div>
</div>
<div class="abs center" style="left:538px;top:770px">
  <div class="circle service-icon" style="background:linear-gradient(135deg,#c9b39f,#6e5f5a)" role="img" aria-label="Photo of a pregnancy consultation"></div>
  <div class="tag" style="margin-top:12px">Prepregnancy<br>Health Check</div>
</div>
<div class="abs center" style="left:718px;top:770px">
  <div class="circle service-icon" style="background:linear-gradient(135deg,#f3eef6,#c7b7d6)" role="img" aria-label="Photo of a smiling doctor"></div>
  <div class="tag" style="margin-top:12px">Fertility<br>Health Check</div>
</div>

<!-- band 1 -->
<div class="abs band" style="top:960px;height:260px;clip-path:polygon(0 8%,100% 0,100% 72%,50% 100%,0 80%);background:linear-gradient(90deg,#ececf0,#d9cfe3 40%,#e4eedf 70%,#d7e6cf)" role="img" aria-label="Blurred photo of women outdoors"></div>
<svg class="abs edge" style="top:955px;height:270px" viewBox="0 0 1200 270" preserveAspectRatio="none" fill="none">
  <path d="M0 26 L1200 5" stroke="#886aae" stroke-width="4"/>
  <path d="M0 213 L600 264 L1200 192" stroke="#886aae" stroke-width="4"/>
</svg>
<div class="abs circle" style="left:270px;top:1065px;width:160px;height:160px;background:linear-gradient(135deg,#f4e9e0,#c9a98f)" role="img" aria-label="Portrait photo of a smiling woman"></div>

<!-- services -->
<div class="abs center" style="left:0;top:1245px;width:1200px">
  <div class="heading">Healthcare <span>Services</span></div>
</div>
<p class="abs copy center" style="left:300px;top:1292px;width:600px">We provide a full range of general and specialist women's health services in a calm, welcoming setting. Each visit is shaped around your needs so you leave informed and supported.</p>
<div class="abs center service-card" style="left:250px;top:1380px">
  <div class="circle" style="background:linear-gradient(135deg,#e5d3e4,#b59cc6)" role="img" aria-label="Photo of a woman stretching"></div>
  <div class="abs badge" style="left:0;top:100px">Well<br>Woman</div>
  <p class="copy">Lorem ipsum is simply dummy text of the printing and typesetting industry.</p>
  <span class="btn" style="margin-top:12px">Read More</span>
</div>
<div class="abs center service-card" style="left:440px;top:1380px">
  <div class="circle" style="background:linear-gradient(135deg,#e9d9d0,#a88e86)" role="img" aria-label="Photo of a pregnant woman"></div>
  <div class="abs badge" style="left:0;top:100px">Maternal<br>Care</div>
  <p class="copy">Lorem ipsum is simply dummy text of the printing and typesetting industry.</p>
  <span class="btn" style="margin-top:12px">Read More</span>
</div>
<div class="abs center service-card" style="left:630px;top:1380px">
  <div class="circle" style="background:linear-gradient(135deg,#efe7dd,#bfae9e)" role="img" aria-label="Photo of a woman in a bright room"></div>
  <div class="abs badge" style="left:0;top:100px">Pregnancy<br>Check</div>
  <p class="copy">Lorem ipsum is simply dummy text of the printing and typesetting industry.</p>
  <span class="btn" style="margin-top:12px">Read More</span>
</div>
<div class="abs center service-card" style="left:820px;top:1380px">
  <div class="circle" style="background:linear-gradient(135deg,#dfe6ee,#8fa6c0)" role="img" aria-label="Photo of a woman holding her belly"></div>
  <div class="abs badge" style="left:0;top:100px">Fertility<br>Health</div>
  <p class="copy">Lorem ipsum is simply dummy text of the printing and typesetting industry.</p>
  <span class="btn" style="margin-top:12px">Read More</span>
</div>

<!-- band 2 -->
<div class="abs band" style="top:1710px;height:290px;clip-path:polygon(0 0,50% 30%,100% 0,100% 80%,50% 100%,0 80%);background:linear-gradient(90deg,#8a6aaa,#c7b2d8 35%,#efe9f3 55%,#c9d9b9 80%,#9fb988)" role="img" aria-label="Blurred photo of flowers and greenery"></div>
<svg class="abs edge" style="top:1705px;height:300px" viewBox="0 0 1200 300" preserveAspectRatio="none" fill="none">
  <path d="M0 237 L600 295 L1200 237" stroke="#886aae" stroke-width="4"/>
</svg>
<div class="abs circle" style="left:515px;top:1760px;width:170px;height:170px;background:linear-gradient(135deg,#f0e4dc,#b8957c)" role="img" aria-label="Portrait photo of a woman"></div>

<!-- blog -->
<div class="abs center" style="left:0;top:1975px;width:1200px">
  <div class="heading"><span>Our</span> Blog</div>
</div>
<svg class="abs arrow" style="left:262px;top:2090px" viewBox="0 0 20 30"><path d="M16 3 L4 15 L16 27" stroke="#886aae" stroke-width="4" fill="none"/></svg>
<svg class="abs arrow" style="left:918px;top:2090px" viewBox="0 0 20 30"><path d="M4 3 L16 15 L4 27" stroke="#886aae" stroke-width="4" fill="none"/></svg>
<div class="abs post" style="left:312px;top:2040px">
  <div style="height:130px;background:linear-gradient(135deg,#b9d49b,#6f9a52)" role="img" aria-label="Photo of a woman doing yoga on grass"></div>
  <h4>Lorem ipsum is simply dummy text of the</h4>
  <p class="copy" style="font-size:11px">Lorem ipsum is simply dummy text of the printing and typesetting industry.</p>
  <span class="btn" style="margin-top:12px">Read More</span>
</div>
<div class="abs post" style="left:510px;top:2040px">
  <div style="height:130px;background:linear-gradient(135deg,#e8dcd2,#9a8474)" role="img" aria-label="Photo of a woman with a child"></div>
  <h4>Lorem ipsum is simply dummy text of the</h4>
  <p class="copy" style="font-size:11px">Lorem ipsum is simply dummy text of the printing and typesetting industry.</p>
  <span class="btn" style="margin-top:12px">Read More</span>
</div>
<div class="abs post" style="left:708px;top:2040px">
  <div style="height:130px;background:linear-gradient(135deg,#f1e1d3,#c39a7c)" role="img" aria-label="Photo of a smiling mature woman"></div>
  <h4>Lorem ipsum is simply dummy text of the</h4>
  <p class="copy" style="font-size:11px">Lorem ipsum is simply dummy text of the printing and typesetting industry.</p>
  <span class="btn" style="margin-top:12px">Read More</span>
</div>

<!-- band 3 -->
<div class="abs band" style="top:2340px;height:270px;clip-path:polygon(0 0,100% 22%,100% 100%,0 72%);background:linear-gradient(90deg,#d7e9f3,#eef4f8 40%,#e2dcec 70%,#cdbfe0)" role="img" aria-label="Soft photo of a bright clinic interior"></div>
<svg class="abs edge" style="top:2335px;height:280px" viewBox="0 0 1200 280" preserveAspectRatio="none" fill="none">
  <path d="M0 5 L1200 64" stroke="#886aae" stroke-width="4"/>
  <path d="M0 199 L1200 275" stroke="#d3a5cc" stroke-width="3"/>
</svg>
<div class="abs circle" style="left:745px;top:2405px;width:170px;height:170px;background:linear-gradient(135deg,#f3ece6,#b7a392)" role="img" aria-label="Portrait photo of a female doctor"></div>

<!-- social -->
<div class="abs center" style="left:0;top:2618px;width:1200px">
  <div class="heading" style="font-size:26px"><span>Join our</span> Social Circle</div>
</div>
<div class="abs center social" style="left:270px;top:2680px">
  <div class="dot" style="background:#5bb8e8"></div>
  <div class="name">Chirply</div>
  <p>Lorem ipsum dolor sit amet, consectetur adipiscing elit sed do eiusmod.</p>
  <p>Tempor incididunt ut labore et dolore magna aliqua.</p>
</div>
<div class="abs center social" style="left:490px;top:2680px">
  <div class="dot" style="background:var(--blue)"></div>
  <div class="name">Aurelle Women's Health</div>
  <p>Like us on Friendwall<br>Like us to see daily updates</p>
  <p>Friendwall</p>
</div>
<div class="abs center social" style="left:710px;top:2680px">
  <div class="dot" style="background:#d9534f"></div>
  <div class="name">Aurelle Women's Health</div>
  <p>Follow us on Plivora<br>Find us here</p>
  <p>Plivora</p>
</div>

<!-- bottom diagonal -->
<svg class="abs edge" style="top:2870px;height:180px" viewBox="0 0 1200 180" preserveAspectRatio="none">
  <path d="M0 30 L600 140 L1200 30 L1200 180 L0 180Z" fill="#f1f1f3"/>
  <path d="M0 10 L600 125 L1200 10" stroke="#886aae" stroke-width="4" fill="none"/>
  <path d="M0 40 L600 150 L1200 40" stroke="#d3a5cc" stroke-width="2" fill="none"/>
</svg>
<div class="abs circle" style="left:556px;top:2960px;width:88px;height:88px;background:radial-gradient(circle at 40% 35%,var(--white),var(--lilac) 60%,var(--violet))" role="img" aria-label="Clinic emblem"></div>

<!-- footer -->
<div class="abs footer"></div>
<div class="abs fcol" style="left:150px;top:3070px">
  <h5>Sitemap</h5>
  <ul><li>Home</li><li>Healthcare Services</li><li>Team</li><li>Fees</li><li>Blog</li></ul>
</div>
<div class="abs fcol" style="left:270px;top:3094px">
  <ul><li>Fees</li><li>Testimonials</li><li>Videos</li><li>E-book</li><li>Contact</li></ul>
</div>
<div class="abs fcol" style="left:420px;top:3070px">
  <h5>Connect</h5>
  <ul><li>Friendwall</li><li>Chirply</li><li>Plivora</li></ul>
</div>
<div class="abs fcol" style="left:560px;top:3070px">
  <h5>Services</h5>
  <ul><li>12 Harbour Lane</li><li>Northbay NSW 2000</li><li>(02) 4000 1234</li><li>info@aurellehealth.com</li></ul>
</div>
<div class="abs subscribe">
  <div class="fcol"><h5 style="margin-bottom:2px">Subscribe to our newsletter</h5></div>
  <input type="text" value="Email" aria-label="Email">
  <input type="text" value="Address" aria-label="Address">
  <span class="btn">Subscribe</span>
</div>
<div class="abs bottombar">© 2015 Aurelle Women's Health. All rights reserved.</div>

</body>
</html>
```